Wedding Photography business card

I need a business card made for a wedding photography business. Formal, unique, i like dark colors maybe black, white, gray, deep blue, silver. Sharp.

This is an idea i have i don't know if it would work.
Think Palm Beach, florida

work in mirror mode in your design program, Just an idea

Front side:
feminine, classy maybe white from wedding dress,
script, elegant,

back side:
masculine, black from tux, symbolizing strength, power,
serif

RK Photography
(561) 430-2917
www.rolfkphoto.example

Target Market(s)

upscale Weddings, targeting bride and groom

Industry/Entity Type

Wedding

Font styles to use
Serif
Script

Colors

Designer to choose colors to be used in the design.

Requirements
Must have
• both sides match somehow

```html
<!DOCTYPE html>
<html lang="en">
<head>
<meta charset="utf-8">
<title>RK Photography – Business Card Back</title>
<link rel="stylesheet" href="https://fonts.googleapis.com/css2?family=Comfortaa:wght@500&display=swap">
<style>
  :root {
    --jacket: #3d3a35;
    --lapel: #2e2c2d;
    --shirt: #e9e7e2;
    --tie: #615a4c;
    --type-fill: #9aaaa6;
    --type-edge: #2c3736;
  }
  html, body {
    margin: 0;
    padding: 0;
    overflow: hidden;
    background: var(--jacket);
  }
  .card {
    position: relative;
    width: 1200px;
    height: 702px;
    overflow: hidden;
  }
  .tuxedo-art {
    position: absolute;
    inset: 0;
    background: linear-gradient(150deg,
      var(--jacket) 0%,
      var(--lapel) 30%,
      var(--shirt) 52%,
      var(--lapel) 74%,
      var(--jacket) 100%);
  }
  .contact {
    position: absolute;
    left: 0;
    right: 0;
    top: 244px;
    margin: 0;
    text-align: center;
    font-family: 'Comfortaa', sans-serif;
    font-weight: 500;
    font-size: 56px;
    line-height: 78px;
    letter-spacing: 0.5px;
    color: var(--type-fill);
    -webkit-text-stroke: 2px var(--type-edge);
    paint-order: stroke fill;
  }
  .contact span { display: block; }
  .contact .web { font-size: 54px; }
</style>
</head>
<body>
<div class="card">
  <div class="tuxedo-art" role="img" aria-label="Flat geometric tuxedo illustration: dark jacket and lapels, white shirt front with tan studs, and a bow tie"></div>
  <p class="contact">
    <span class="name">RK Photography</span>
    <span class="phone">(561) 430-2917</span>
    <span class="web">www.rolfkphoto.example</span>
  </p>
</div>
</body>
</html>
```